Satin Decor Paint Label

We will have three different sizes for this label but the dimensions for the medium size are 2" tall by 11.75'' wide. Please work off that.

Our colors are typically black and white but feel free to incorporate silver, gold, bronze or any combination. We would like to see multiple color variations of your designs.

General Info needed on label:
4627
Coatings
Interior Decor Paint
Furniture, Trim, Cabinets
Acrylic Waterborne Urethane
Satin Finish
16 FL. OZ. - 473 mL
````````````````````````````````````````````````````````````````````````````````````````````
Your design does not have to be the same as the one in the attached image.

You can put Satin Finish or Interior Decor Paint or something else going vertically up the side.

The label will be on a container like the the one in the attached image. Please have your design work on the same container.

```html
<!DOCTYPE html>
<html lang="en">
<head>
<meta charset="utf-8">
<title>4627 Coatings – Satin Decor Paint Label</title>
<link href="https://fonts.googleapis.com/css2?family=Fira+Sans+Condensed:wght@300;400;600&display=swap" rel="stylesheet">
<style>
  :root {
    --backdrop: #e4e4e4;
    --label-white: #fbfbfb;
    --ink: #0d0d0d;
    --silver: #d2d2d2;
    --rule: #1a1a1a;
  }
  * { margin: 0; padding: 0; box-sizing: border-box; }
  html, body { width: 849px; height: 1200px; overflow: hidden; }
  body {
    background: var(--backdrop);
    font-family: "Fira Sans Condensed", sans-serif;
    color: var(--ink);
    position: relative;
  }
  .label {
    position: absolute;
    left: 74px; top: 400px;
    width: 700px; height: 420px;
    background: var(--label-white);
  }
  .brand-block {
    position: absolute;
    left: 175px; top: 40px;
    width: 320px; height: 230px;
    background: var(--ink);
    color: var(--silver);
    text-align: center;
    font-weight: 300;
  }
  .brand-number {
    display: block;
    font-size: 150px;
    line-height: 1;
    margin-top: 12px;
    letter-spacing: 2px;
  }
  .brand-word {
    display: block;
    font-size: 40px;
    letter-spacing: 9px;
    margin-top: 4px;
  }
  .use-panel {
    position: absolute;
    left: 175px; top: 270px;
    width: 320px; height: 78px;
    border: 1.5px solid var(--rule);
    border-top: none;
    text-align: center;
    font-size: 19px;
    line-height: 1.3;
    padding-top: 8px;
    letter-spacing: 0.4px;
  }
  .finish-tab {
    position: absolute;
    left: 247px; top: 338px;
    width: 176px; height: 28px;
    background: var(--ink);
    color: #fff;
    font-weight: 600;
    font-size: 17px;
    letter-spacing: 0.8px;
    text-align: center;
    line-height: 28px;
  }
  .volume {
    position: absolute;
    left: 175px; top: 374px;
    width: 320px;
    text-align: center;
    font-size: 17px;
    letter-spacing: 0.4px;
  }
  .side-line {
    position: absolute;
    left: 525px; top: 40px;
    height: 308px;
    writing-mode: vertical-rl;
    transform: rotate(180deg);
    font-size: 25px;
    font-weight: 400;
    letter-spacing: 1.5px;
    text-align: center;
  }
</style>
</head>
<body>
  <section class="label">
    <div class="brand-block">
      <span class="brand-number">4627</span>
      <span class="brand-word">COATINGS</span>
    </div>
    <div class="use-panel">
      FURNITURE, TRIM, CABINETS<br>
      ACRYLIC WATERBORNE URETHANE
    </div>
    <div class="finish-tab">SATIN FINISH</div>
    <p class="volume">16 FL. OZ. - 473 mL</p>
    <p class="side-line">INTERIOR DECOR PAINT</p>
  </section>
</body>
</html>
```